Lumen Hall of Music Website Design

Lumen Hall of Music would like to have a website designed. They are a new business similar to Quorvale (https://quorvaletunes.example).

We prefer using Adobe Fonts throughout the design. Kepler was used for the logo. Lorem Ipsum is fine to use except for headers.

Please keep track of any images/icons that are used in your design. We plan on purchasing the images used in the winning design.

Target Market(s)

Children age 10 - 18

Number of Pages Required

1 page

Font styles to use
Sans Serif

Colors
0054AA
0677BA
7BADD7
CADEEF
E8F1F8

```html
<!DOCTYPE html>
<html lang="en">
<head>
<meta charset="utf-8">
<title>Lumen Hall of Music</title>
<link href="https://fonts.googleapis.com/css2?family=Kanit:wght@400;600&family=Catamaran:wght@400;500;700&family=Crimson+Text&display=swap" rel="stylesheet">
<style>
:root{
  --backdrop:#6f6f6f;
  --ink:#1a1a1a;
  --white:#ffffff;
  --soft:#f8f8f8;
  --line:#d8d8d8;
  --grey-band:#6b6b6b;
  --footer:#141414;
  --accent:#c0883c;
  --muted:#666;
}
*{margin:0;padding:0;box-sizing:border-box}
html,body{width:1200px;height:2207px;overflow:hidden}
body{background:var(--backdrop);font-family:"Catamaran",sans-serif;color:var(--ink);position:relative}
.site{position:absolute;left:143px;top:192px;width:916px;height:1822px;border-radius:10px;overflow:hidden;background:var(--white)}
.abs{position:absolute}

/* hero */
.hero{left:0;top:0;width:916px;height:515px;background:radial-gradient(ellipse at 55% 40%,#4a3626 0%,#2a1e16 40%,#120e0c 80%)}
.brand{left:143px;top:28px;display:flex;align-items:center;gap:8px;color:var(--white);font-family:"Catamaran",sans-serif;font-weight:700;font-size:17px;letter-spacing:1px}
.brand-mark{width:14px;height:14px;background:var(--white)}
.nav{left:321px;top:64px;display:flex;gap:0;font-size:10px;color:var(--white)}
.nav a{color:inherit;text-decoration:none;position:absolute;white-space:nowrap}
.utility{left:684px;top:37px;display:flex;align-items:center;gap:8px;color:var(--white);font-size:6px}
.hero-title{left:143px;top:196px;font-family:"Kanit",sans-serif;font-weight:600;font-size:41px;line-height:43px;color:var(--white);letter-spacing:.5px}
.hero-text{left:143px;top:296px;width:360px;font-family:"Crimson Text",serif;font-size:13px;line-height:18px;color:#e9e2da}
.hero-btn{left:143px;top:368px;width:177px;height:54px;border:1px solid var(--white);color:var(--white);font-family:"Kanit",sans-serif;font-size:11px;letter-spacing:1px;display:flex;align-items:center;justify-content:center}
.dots{left:713px;top:479px;display:flex;gap:5px}
.dots span{width:8px;height:8px;border-radius:50%;border:1px solid #888}
.dots .on{background:var(--accent);border-color:var(--accent);width:9px;height:9px}

/* awards */
.awards{left:0;top:515px;width:916px;height:170px;background:var(--soft)}
.awards svg{position:absolute;top:60px}

/* programs */
.programs{left:0;top:685px;width:916px;height:397px;background:var(--white)}
.card{top:48px;width:198px;height:267px;background:var(--white);box-shadow:0 1px 4px rgba(0,0,0,.15)}
.card-media{width:198px;height:171px;background:linear-gradient(180deg,#1f2a38 0%,#1f2a38 35%,#9aa2ad 100%)}
.card-media.fade{background:linear-gradient(90deg,#1f2a38 0%,#9aa2ad 50%,#ffffff 100%)}
.card-title{position:absolute;left:24px;top:192px;font-family:"Kanit",sans-serif;font-weight:600;font-size:11px;letter-spacing:.3px}
.card-sub{position:absolute;left:24px;top:210px;font-size:10px}
.card.faded .card-title{color:#555}.card.faded .card-sub{color:#555}
.scrollbar{left:143px;top:551px;width:630px;height:3px;background:var(--line);border-radius:2px}
.scrollbar span{position:absolute;left:0;top:0;width:60px;height:3px;background:#999}

/* testimonial */
.testimonial{left:0;top:1082px;width:916px;height:338px;background:var(--soft)}
.quote-card{left:143px;top:65px;width:630px;height:205px;background:var(--white);box-shadow:0 1px 3px rgba(0,0,0,.12)}
.quote-photo{left:0;top:0;width:205px;height:205px;background:linear-gradient(160deg,#4b3b33 0%,#a9787c 55%,#6c2a35 100%)}
.quote-name{left:265px;top:40px;font-family:"Kanit",sans-serif;font-size:12px;font-weight:400;letter-spacing:.3px}
.quote-text{left:265px;top:66px;width:300px;font-size:10px;line-height:15.5px}
.quote-role{left:265px;top:155px;font-family:"Crimson Text",serif;font-size:8px;color:#bbb}
.info-icon{left:601px;top:10px}

/* information */
.information{left:0;top:1420px;width:916px;height:342px;background:var(--grey-band);color:var(--white);text-align:center}
.information h2{position:absolute;left:0;width:916px;top:66px;font-family:"Kanit",sans-serif;font-weight:400;font-size:28px;letter-spacing:1px}
.information .rule{left:405px;top:102px;width:106px;height:1px;background:#bdbdbd}
.information p{position:absolute;left:138px;width:640px;top:136px;font-size:14.5px;line-height:25px}
.read-btn{left:397px;top:438px;width:121px;height:37px;background:var(--white);color:#333;font-size:12px;display:flex;align-items:center;justify-content:center;letter-spacing:.5px}
.information .read-btn{top:438px;position:absolute}
.footer{left:0;top:1762px;width:916px;height:60px;background:var(--footer)}
</style>
</head>
<body>
<div class="site">
  <header class="hero abs" role="img" aria-label="Photo of a young cellist performing with an orchestra">
    <div class="brand abs"><span class="brand-mark"></span>LUMEN</div>
    <nav class="nav abs">
      <a style="left:0">Our Programs</a>
      <a style="left:98px">About Us</a>
      <a style="left:173px">Our Impact</a>
      <a style="left:257px">Support Lumen</a>
      <a style="left:369px">Student Resources</a>
    </nav>
    <div class="utility abs">
      <svg width="11" height="11" viewBox="0 0 12 12" fill="none" stroke="#fff" stroke-width="1.3"><circle cx="5" cy="5" r="3.6"/><path d="M7.7 7.7L11 11"/></svg>
      <svg width="11" height="11" viewBox="0 0 12 12" fill="none" stroke="#fff" stroke-width="1"><circle cx="6" cy="6" r="5"/><path d="M1 6h10M6 1c-3 3-3 7 0 10M6 1c3 3 3 7 0 10"/></svg>
      <svg width="11" height="11" viewBox="0 0 12 12" fill="none" stroke="#fff" stroke-width="1"><circle cx="6" cy="6" r="5"/><circle cx="6" cy="5" r="1.8"/><path d="M2.8 9.6c1.8-2 4.6-2 6.4 0"/></svg>
      <span>My Account ▾</span>
    </div>
    <h1 class="hero-title abs">LUMEN HALL<br>OF MUSIC</h1>
    <p class="hero-text abs">removes barriers to high-quality music education so that all children can experience the transformative power of music.</p>
    <div class="hero-btn abs">MORE INFORMATIONS</div>
    <div class="dots abs"><span></span><span></span><span class="on"></span><span></span><span></span></div>
  </header>

  <section class="awards abs" aria-label="Awards">
    <svg style="left:313px" width="48" height="60" viewBox="0 0 48 60" fill="none" stroke="#111" stroke-width="3"><circle cx="24" cy="22" r="19"/><path d="M24 12l3 7 7 .5-5.5 4.5 2 7-6.5-4-6.5 4 2-7-5.5-4.5 7-.5z" fill="#111" stroke="none"/><path d="M10 35v20l14-7 14 7V35"/></svg>
    <svg style="left:393px" width="48" height="60" viewBox="0 0 48 60" fill="none" stroke="#111" stroke-width="3"><circle cx="24" cy="22" r="19"/><path d="M24 12l3 7 7 .5-5.5 4.5 2 7-6.5-4-6.5 4 2-7-5.5-4.5 7-.5z" fill="#111" stroke="none"/><path d="M10 35v20l14-7 14 7V35"/></svg>
    <svg style="left:474px" width="48" height="60" viewBox="0 0 48 60" fill="none" stroke="#111" stroke-width="3"><circle cx="24" cy="22" r="19"/><path d="M24 12l3 7 7 .5-5.5 4.5 2 7-6.5-4-6.5 4 2-7-5.5-4.5 7-.5z" fill="#111" stroke="none"/><path d="M10 35v20l14-7 14 7V35"/></svg>
    <svg style="left:553px" width="48" height="60" viewBox="0 0 48 60" fill="none" stroke="#111" stroke-width="3"><circle cx="24" cy="22" r="19"/><path d="M24 12l3 7 7 .5-5.5 4.5 2 7-6.5-4-6.5 4 2-7-5.5-4.5 7-.5z" fill="#111" stroke="none"/><path d="M10 35v20l14-7 14 7V35"/></svg>
  </section>

  <section class="programs abs" aria-label="Programs">
    <article class="card abs" style="left:143px">
      <div class="card-media" role="img" aria-label="Image placeholder for early childhood program"></div>
      <h3 class="card-title">EARLY CHILDHOOD</h3>
      <p class="card-sub">Newborns – 8 years</p>
    </article>
    <article class="card abs" style="left:359px">
      <div class="card-media" role="img" aria-label="Image placeholder for private lessons"></div>
      <h3 class="card-title" style="top:195px">PRIVATE LESSONS</h3>
      <p class="card-sub" style="top:213px">Ages 4+</p>
    </article>
    <article class="card faded abs" style="left:575px">
      <div class="card-media fade" role="img" aria-label="Image placeholder for group classes"></div>
      <h3 class="card-title" style="top:195px">GROUP CLASSES</h3>
      <p class="card-sub" style="top:213px">Ages 6+</p>
    </article>
    <div class="scrollbar abs"><span></span></div>
  </section>

  <section class="testimonial abs" aria-label="Testimonial">
    <div class="quote-card abs">
      <div class="quote-photo abs" role="img" aria-label="Portrait of a student holding a flute beside a piano"></div>
      <svg class="info-icon abs" width="16" height="16" viewBox="0 0 16 16" fill="none" stroke="#222" stroke-width="1.2"><circle cx="8" cy="8" r="7"/><path d="M8 7v5"/><circle cx="8" cy="4.6" r=".6" fill="#222"/></svg>
      <h4 class="quote-name abs">JANE DOE</h4>
      <p class="quote-text abs">“Lumen has changed my life.<br>It’s changed the entire trajectory of where I’m going, who I believe I am. Lumen has given me these opportunities, this vision, this hope for a better dream of myself.”</p>
      <p class="quote-role abs">Lumen Alumni</p>
    </div>
  </section>

  <section class="information abs">
    <h2>INFORMATION</h2>
    <div class="rule abs"></div>
    <p>There are many variations of passages of Lorem Ipsum available, but the majority have suffered alteration in some form, by injected humour, or randomised words which don’t look even slightly believable.</p>
    <div class="read-btn">READ MORE</div>
  </section>

  <footer class="footer abs"></footer>
</div>
</body>
</html>
```